Visual Print Advert for Hair & Makeup Artist

One page colour visual advertisement required for a hair and makeup artist business using pictures and logo with brief description and contact details. MUST have plain white background. All information will be provided I just need someone to put it in a good layout.
Professional, clean and appealing to the eye. Don't want it to look over crowded or busy.
Layout should feature 2-7 photos, without making the page look too busy. Can use any of the photos provided and you are welcome to crop them to change the orientation of the photo.
Content and typeface should fit in with logo and be modern but appeal to the female target audience of brides in Australia aged 22-40yo.
Advertisement is be be used in a bridal magazine and other print media for business advertising purposes.
Updates

Ad is to be A4 size, portrait orientation Added Monday, December 26, 2016

Target Market(s)

Future brides in Australia aged 22 - 40yo - females only

Industry/Entity Type

Business

Colors
e34197
ffffff
eda3c7

Requirements
Must have
• White background
Should not have
• NO script writing as it doesn't fit with the logo.

```html
<!DOCTYPE html>
<html lang="en">
<head>
<meta charset="utf-8">
<title>Aurelle Makeup Artistry – Bridal Makeup &amp; Hair</title>
<link rel="stylesheet" href="https://fonts.googleapis.com/css2?family=Noto+Sans+Mono:wght@400;500&family=Open+Sans:wght@400;700&display=swap">
<style>
  :root {
    --pink: #e34197;
    --pink-soft: #eda3c7;
    --ink: #1c1c1c;
    --logo-ink: #2b2b2b;
    --rule: #b5b5b5;
    --paper: #ffffff;
    --mono: "Noto Sans Mono", monospace;
    --sans: "Open Sans", sans-serif;
  }
  * { margin: 0; padding: 0; box-sizing: border-box; }
  html, body { width: 848px; height: 1200px; overflow: hidden; background: var(--paper); }
  .advert { position: relative; width: 848px; height: 1200px; background: var(--paper); color: var(--ink); font-family: var(--mono); }

  .brand-name {
    position: absolute; left: 74px; top: 46px;
    font-family: var(--mono); font-weight: 400; font-size: 128px; line-height: 1;
    letter-spacing: 24px; color: var(--logo-ink);
  }
  .brand-tagline {
    position: absolute; right: 78px; top: 168px;
    font-family: var(--sans); font-weight: 400; font-size: 28px; letter-spacing: 5px;
    color: var(--logo-ink);
  }

  .intro, .promise {
    position: absolute; left: 0; width: 848px; text-align: center;
    font-size: 22px; letter-spacing: 1.5px; line-height: 30.5px; text-transform: uppercase;
  }
  .intro { top: 232px; }
  .promise { top: 954px; }
  .promise .accent { color: var(--pink); }

  .rule { position: absolute; left: 178px; width: 580px; height: 1px; background: var(--rule); }
  .rule--top { top: 346px; }
  .rule--bottom { top: 927px; }

  .photo { position: absolute; }
  .photo--hero {
    left: 229px; top: 360px; width: 272px; height: 539px;
    background: linear-gradient(180deg, #f7ede4 0%, #e9d3c0 30%, #f2ece6 55%, #e8e0d6 80%, #efe9e2 100%);
  }
  .photo--one { left: 551px; top: 370px; width: 248px; height: 165px;
    background: linear-gradient(135deg, #f2f2f2 0%, #9a9a9a 55%, #dcdcdc 100%); }
  .photo--two { left: 551px; top: 552px; width: 247px; height: 164px;
    background: linear-gradient(135deg, #6e6577 0%, #c8bcc8 50%, #8a7e8c 100%); }
  .photo--three { left: 553px; top: 733px; width: 246px; height: 163px;
    background: linear-gradient(180deg, #9a9a9a 0%, #5a5a5a 60%, #222 100%); }

  .gallery-line { position: absolute; left: 538px; top: 371px; width: 2px; height: 526px; background: #333; }

  .headline { position: absolute; left: 74px; top: 545px; }
  .headline__main {
    display: block; font-family: var(--mono); font-weight: 500; font-size: 86px; line-height: 1;
    letter-spacing: 4px; color: var(--pink);
  }
  .headline__sub {
    display: block; margin-top: 2px; font-family: var(--mono); font-size: 44px; line-height: 1;
    color: #000;
  }

  .contact { position: absolute; left: 0; width: 848px; text-align: center; font-family: var(--sans); color: var(--ink); }
  .contact__line { top: 1102px; font-size: 22px; }
  .contact__label { color: var(--pink-soft); font-weight: 700; }
  .contact__web { top: 1134px; font-size: 22px; font-weight: 700; letter-spacing: 0.5px; }
</style>
</head>
<body>
<main class="advert">
  <div class="brand-name">AURELLE</div>
  <div class="brand-tagline">MAKEUP ARTISTRY</div>

  <p class="intro">Professionally trained and certified<br>mobile hair &amp; makeup artists with<br>over 10 years experience.</p>

  <div class="rule rule--top"></div>

  <div class="photo photo--hero" role="img" aria-label="Bride in a lace dress holding a bouquet of cream roses"></div>
  <h1 class="headline">
    <span class="headline__main">BRIDAL</span>
    <span class="headline__sub">makeup &amp; hair</span>
  </h1>

  <div class="gallery-line"></div>
  <div class="photo photo--one" role="img" aria-label="Black and white portrait of a bride in a veil and pearls"></div>
  <div class="photo photo--two" role="img" aria-label="Colour portrait of a bride with soft makeup and veil"></div>
  <div class="photo photo--three" role="img" aria-label="Black and white photo of a bride laughing with her bridesmaids"></div>

  <div class="rule rule--bottom"></div>

  <p class="promise">We specialise in naturally<br>enhancing your beauty to have you<br>looking and feeling your best<br><span class="accent">on your special day.</span></p>

  <p class="contact contact__line"><span class="contact__label">t:</span> 0400 123 456 | <span class="contact__label">e:</span> mia@aurellemakeup.com.au</p>
  <p class="contact contact__web">www.aurellemakeup.com.au</p>
</main>
</body>
</html>
```